Buch-/E-Book-Cover für Referenzbuch der Industrie
Zielgruppe
Als Manufaktur einzigartiger Fachmedien präsentiert verlag-wendemark Schlüsseltechnologien und ihre Märkte. Faszination für Technik ist die Grundlage unserer Arbeit. Mehr als 30 Jahre verlegerische Erfahrung und das Verständnis für Technologiemärkte machen uns zu einem anerkannten Partner der Industrie.
Unsere Medienmarken knüpfen ein starkes und weit verzweigtes Netzwerk – Print und digital – , in dem sich Anbieter und Anwender von Technologien und Produkten in ihren Zielsetzungen wiederfinden.
Unsere Magazine, Events und Netzwerkveranstaltungen sowie kundenspezifische Kommunikations- & Strategiekampagnen setzen in ihren Zielmärkten Maßstäbe und genießen bei Lesern, Kunden und Partnern Vertrauen und Respekt.
Für das ausgeschriebene Projekt handelt es sich um unsere Referenzpublikation Factory Onward MOLUTAVA.
MOLUTAVA {polynesisch: Freiraum}
Das Referenzbuch der Industrie. Für Vorwärtsdenker und Zukunftsmacher.
Wandel bestimmt unsere Zeit und verändert unsere Gesellschaft, unsere Unternehmen, uns alle.
Im Wandel liegt Freiraum zur Gestaltung. Gesellschaftlicher Wandel, Technologie-Wandel, Klimawandel, Wertewandel, Führungswandel oder Organisationswandel sind nur einige Beispiele. Wer dabei den Wandel in engen Bahnen denkt, verschenkt Potential. Veränderung braucht Freiraum für neue Ideen und Perspektiven sowie Persönlichkeiten, die diesen nutzen wollen.
Aber wer gestaltet die Zukunft der Industrie und ihrer Branchen? Und wie?
Wir geben Personen aus der Industrie den Freiraum, ihre Perspektiven auf und aus dem Wandel zu erzählen. Warum? Weil sie uns begeistert haben, in persönlichen Treffen und Gesprächen, durch streitbare Meinungen und ehrliche Geschichten. Weil sie die Zukunft verändern.
MOLUTAVA ist eine Aufforderung: Zum Mitdenken, Weiterdenken, aber auch Nachdenken.
MOLUTAVA – FREIRAUM FÜR IDEEN
Ein Referenzbuch, d..
Aufgabenstellung
1. Kurzzusammenfassung der Ausschreibung
Die 4. Ausgabe des jährlichen Referenzbuchs der Industrie, Factory Onward MOLUTAVA 2025, erscheint im Oktober 2024. Für das Cover sucht der verlag-wendemark Verlag neue Vorschläge, die die Themen Freiraum und Wandel in den Fokus stellen.
2. Gestalterische & Inhaltliche Anforderungen
• Format: 195x250 mm + Anschnitt
• Rücken: ca. 1,6 cm (Stand letzte Publikation 2023)
• Auflösung: Druckqualität, mind. 300 dpi
• Inhaltliche Elemente:
- MOLUTAVA Schriftzug
- {polynesisch: Freiraum}
- Untersatz: Das Referenzbuch der Industrie. Für Vorwärtsdenker und Zukunftsmacher.
- part of Factory Onward Logo-Balken am unteren Rand (siehe Beispiel AuD_Titelbeispiel_Logobalken)
WICHTIG: Der aktuelle Schriftzug MOLUTAVA und die Farbe Orange (0/80/100/0) (siehe Beispiel MOLUTAVA 2021) sollen als Wiedererkennung in die Gestaltungen eingebunden werden.

```html
<!DOCTYPE html>
<html lang="de">
<head>
<meta charset="utf-8">
<title>MOLUTAVA 2024 – Cover</title>
<link rel="stylesheet" href="https://fonts.googleapis.com/css2?family=Oswald:wght@500;700&family=Barlow:wght@400;600&display=swap">
<style>
  :root {
    --orange: #e64f12;
    --paper: #f5f3ef;
    --white: #ffffff;
    --ink: #3a3a3a;
  }
  html, body {
    margin: 0;
    padding: 0;
    width: 1200px;
    height: 732px;
    overflow: hidden;
    background: var(--white);
  }
  .canvas {
    position: relative;
    width: 1200px;
    height: 732px;
    overflow: hidden;
  }
  .back-cover {
    position: absolute;
    left: 0; top: 0;
    width: 630px; height: 732px;
    background: var(--orange);
  }
  .front-cover {
    position: absolute;
    left: 630px; top: 0;
    width: 570px; height: 732px;
    background: var(--white);
  }
  .cover-art {
    position: absolute;
    left: 0; top: 0;
    width: 570px; height: 693px;
    background: linear-gradient(180deg, #f6f4f0 0%, #efece7 100%);
  }
  .wordmark {
    position: absolute;
    left: 0; top: 0;
    width: 330px; height: 693px;
    overflow: hidden;
  }
  .wordmark text.letters {
    font-family: "Oswald", sans-serif;
    font-weight: 700;
    font-size: 166px;
  }
  .wordmark text.gloss {
    font-family: "Oswald", sans-serif;
    font-weight: 500;
    font-size: 15px;
  }
  .back-cover .letters, .back-cover .gloss { fill: var(--white); }
  .front-cover .letters, .front-cover .gloss { fill: var(--orange); }
  .edition {
    position: absolute;
    left: 270px; top: 366px;
    width: 290px;
    text-align: center;
    color: var(--orange);
    font-family: "Barlow", sans-serif;
  }
  .edition .year {
    margin: 0;
    font-weight: 600;
    font-size: 33px;
    line-height: 36px;
    letter-spacing: 1px;
  }
  .edition .claim {
    margin: 4px 0 0;
    font-weight: 400;
    font-size: 10.5px;
    line-height: 14px;
    letter-spacing: 0.9px;
    text-transform: uppercase;
  }
  .logo-bar {
    position: absolute;
    left: 0; top: 693px;
    width: 570px; height: 39px;
    display: flex;
    align-items: center;
    justify-content: center;
    padding-left: 40px;
    box-sizing: border-box;
    font-family: "Barlow", sans-serif;
    font-weight: 400;
    font-size: 14px;
    color: var(--ink);
    letter-spacing: 0.3px;
  }
</style>
</head>
<body>
<main class="canvas">

  <section class="back-cover" aria-label="Rückseite">
    <svg class="wordmark" width="330" height="693" viewBox="0 0 330 693">
      <text class="letters" x="-8" y="208" textLength="162" lengthAdjust="spacingAndGlyphs">MO</text>
      <text class="letters" x="-8" y="352" textLength="162" lengthAdjust="spacingAndGlyphs">LU</text>
      <text class="gloss" x="7" y="372">{polynesisch – Freiraum}</text>
      <text class="letters" x="-8" y="514" textLength="162" lengthAdjust="spacingAndGlyphs">TA</text>
      <text class="letters" x="-8" y="657" textLength="162" lengthAdjust="spacingAndGlyphs">VA</text>
    </svg>
  </section>

  <section class="front-cover" aria-label="Titelseite">
    <div class="cover-art" role="img" aria-label="Bleistiftzeichnung: Vögel fliegen über einen Maschendrahtzaun in die Freiheit"></div>

    <svg class="wordmark" width="330" height="693" viewBox="0 0 330 693">
      <rect x="0" y="352" width="163" height="28" fill="var(--white)"/>
      <text class="letters" x="-8" y="208" textLength="162" lengthAdjust="spacingAndGlyphs">MO</text>
      <text class="letters" x="-8" y="352" textLength="162" lengthAdjust="spacingAndGlyphs">LU</text>
      <text class="gloss" x="7" y="372">{polynesisch – Freiraum}</text>
      <text class="letters" x="-8" y="514" textLength="162" lengthAdjust="spacingAndGlyphs">TA</text>
      <text class="letters" x="-8" y="657" textLength="162" lengthAdjust="spacingAndGlyphs">VA</text>
    </svg>

    <div class="edition">
      <p class="year">2024</p>
      <p class="claim">Das Referenzbuch der Industrie.<br>Für Vorwärtsdenker und<br>Zukunftsmacher.</p>
    </div>

    <footer class="logo-bar">part of Factory Onward</footer>
  </section>

</main>
</body>
</html>
```